依頼詳細
■地域系LP(PC・スマホサイト)
ページ数:各1ページづつ作成
ワイヤーフレーム:あり
https://pelvix.com/diagrams/RaqM8WbNpe4kV2sY#913KD

※メイン画像部分は写真を入れ込んでデザインお願いします。
(それ以外の素材は支給頂ける予定)
※有料画像を使用する場合は画像の費用は自己負担でお願いします。
※PC、スマホ版ともにデザインの方向性は合わせてください。
※スマホ版は幅640pxで作成お願いします。

■デザイン参考サイト
https://mosuplint.jp/
https://mosuplint.jp/lp/sp/300aa/00/00/00/

■コーディング
一切不要。

■ページ数
PC1ページ
スマホ1ページ
■納品
画像データと制作ファイルを納品ください。
(それ以外の素材は支給頂ける予定)
※スマホ版は幅640pxで作成お願いします。
■ 選んだ理由

情報の伝わりやすいさ、すっきりとしたデザインを評価させていただきました。

■ 提案者全員のお礼・コメント

ご応募くださり、ありがとうございます。
また次回のデザインコンペにもご参加いただけますと幸いです。
よろしくお願いいたします。

```html
<!DOCTYPE html>
<html lang="ja">
<head>
<meta charset="utf-8">
<title>モスプリント 東京都 就職カウンセリング</title>
<link href="https://fonts.googleapis.com/css2?family=Noto+Sans+JP:wght@400;500;700;900&display=swap" rel="stylesheet">
<style>
:root{
  --orange:#f39200;
  --orange-dark:#e07800;
  --green:#7cc42a;
  --green-dark:#5ea81a;
  --green-light:#eaf6d8;
  --pink:#e9437b;
  --blue:#1f7fcf;
  --text:#333;
  --muted:#777;
  --line:#dcdcdc;
  --sky:#e9f3fb;
}
*{box-sizing:border-box;margin:0;padding:0}
html,body{width:1200px;height:4432px;overflow:hidden}
body{font-family:"Noto Sans JP",sans-serif;color:var(--text);background:#fff;position:relative}
.section{position:absolute;left:0;width:1200px}
.brand{font-weight:900;color:var(--orange);display:flex;align-items:center;gap:10px;white-space:nowrap}
.brand .dot{width:22px;height:22px;background:var(--orange);border-radius:50%}

/* hero */
.hero{top:0;height:1060px;background:linear-gradient(180deg,#f7fbff 0%,var(--sky) 60%,#fff 100%)}
.hero-city{position:absolute;left:0;top:0;width:1200px;height:700px;background:linear-gradient(180deg,#dbeaf7,#f2f7fc 70%,#fff)}
.hero .brand{position:absolute;left:40px;top:24px;font-size:40px}
.hero-people{position:absolute;left:560px;top:110px;width:330px;height:600px;background:linear-gradient(180deg,#c9d6e3,#8e9fb1);border-radius:6px}
.headline{position:absolute;left:40px;top:150px;width:780px;z-index:1}
.headline .line1{display:flex;align-items:center;font-size:34px;font-weight:900;white-space:nowrap}
.pref{background:var(--blue);color:#fff;padding:4px 16px;margin-right:8px;font-size:52px}
.headline .line2{margin-top:20px;display:inline-block;background:#fff;border:3px solid var(--orange);color:var(--orange);font-size:36px;font-weight:900;padding:6px 20px}
.headline .line3{margin-top:40px;font-size:56px;font-weight:900;white-space:nowrap;text-shadow:0 0 8px #fff}
.headline .line3 em{font-style:normal;color:var(--orange);font-size:96px;background:#fff8e6;padding:0 10px}
.badge-free{position:absolute;left:890px;top:120px;width:250px;height:250px;border-radius:50%;background:var(--pink);color:#fff;text-align:center;padding-top:48px;font-weight:700;font-size:24px;line-height:1.4;border:6px solid #fff;box-shadow:0 4px 12px rgba(0,0,0,.15)}
.badge-free b{display:block;font-size:64px;font-weight:900;line-height:1.2}
.stats{position:absolute;left:40px;top:720px;width:1120px;display:flex;gap:20px}
.stat{flex:1;background:var(--orange);border-radius:8px;padding:6px;text-align:center}
.stat h3{color:#fff;font-size:26px;padding:10px 0 8px}
.stat p{background:#fff;border-radius:4px;font-size:54px;font-weight:900;color:var(--orange);padding:8px 0}
.stat small{font-size:22px;color:var(--text);margin-left:4px}
.hero-note{position:absolute;left:0;top:940px;width:1200px;text-align:center;font-size:30px;font-weight:700}
.hero-note .pref{font-size:40px;padding:2px 12px;margin:0 6px}

/* cta */
.cta{top:1060px;height:280px;background:#f4f4f4;border-top:1px solid var(--line)}
.cta-title{text-align:center;margin-top:34px;font-size:36px;font-weight:900;display:flex;justify-content:center;align-items:center;gap:12px}
.cta-title .pref-text{color:var(--blue)}
.cta-title .brand{font-size:34px;background:#fff;padding:4px 14px;border:2px solid var(--orange);border-radius:6px}
.cta-row{display:flex;justify-content:center;gap:40px;margin-top:34px}
.btn-apply{display:flex;align-items:center;gap:16px;background:var(--pink);color:#fff;border-radius:10px;padding:18px 34px;font-size:28px;font-weight:900;line-height:1.3;box-shadow:0 5px 0 #b52b5b}
.tel{display:flex;align-items:center;gap:16px}
.tel-icon{width:74px;height:74px;border-radius:50%;background:var(--pink);display:flex;align-items:center;justify-content:center}
.tel small{display:block;font-size:20px;font-weight:700}
.tel b{display:block;font-size:52px;font-weight:900;color:var(--pink);line-height:1.1}
.tel span{font-size:16px;color:var(--muted)}

/* rate */
.rate{top:1340px;height:560px;background:linear-gradient(180deg,var(--green-light),#fff)}
.rate-woman{position:absolute;left:160px;top:100px;width:280px;height:370px;background:linear-gradient(180deg,#d9dde2,#9aa4ae);border-radius:6px}
.rate .brand{position:absolute;left:470px;top:60px;font-size:50px;color:var(--green-dark)}
.rate .brand .dot{background:var(--green)}
.rate .brand span.nara{color:var(--text);font-size:34px}
.rate-label{position:absolute;left:470px;top:150px;font-size:66px;font-weight:900;color:var(--green-dark)}
.rate-chart{position:absolute;left:470px;top:260px}
.rate-num{position:absolute;left:690px;top:270px;font-size:150px;font-weight:900;color:var(--orange);line-height:1;white-space:nowrap}
.rate-num small{font-size:50px;color:var(--green-dark)}
.because{position:absolute;left:0;top:470px;width:1200px;height:90px;background:var(--green)}
.because p{text-align:center;color:#fff;font-size:40px;font-weight:900;line-height:90px}
.because svg{position:absolute;left:560px;bottom:-40px}

/* voices */
.voices{top:1900px;height:1000px;background:var(--green)}
.voices-head{margin:80px auto 0;width:1060px;background:#fff;border-radius:10px;padding:30px;display:flex;align-items:center;gap:24px;justify-content:center}
.voices-head .icon{width:80px;height:80px;border-radius:50%;background:var(--orange)}
.voices-head h2{font-size:34px;font-weight:900;line-height:1.5}
.voices-head h2 span{color:var(--orange)}
.voice-list{display:flex;gap:40px;width:1060px;margin:40px auto 0}
.voice{flex:1;background:#fff;border-radius:8px;padding:30px;height:680px}
.voice-top{display:flex;gap:20px;align-items:center;border-bottom:2px dashed var(--line);padding-bottom:20px}
.avatar{width:100px;height:100px;border-radius:50%;background:#ddd;display:flex;align-items:center;justify-content:center}
.voice-top h3{font-size:22px;color:var(--green-dark)}
.voice-top p{font-size:18px;color:var(--muted)}
.voice-body p{font-size:18px;line-height:1.9;margin-top:20px}

/* form */
.form{top:2900px;height:1060px;background:linear-gradient(180deg,#e3ebf2,#f6f8fa 40%,#eef2f5)}
.form-bg{position:absolute;inset:0;background:linear-gradient(180deg,#dde6ee,#f3f6f9 50%,#e8edf1)}
.form-panel{position:absolute;left:150px;top:70px;width:900px;background:#fff;border-radius:8px;box-shadow:0 3px 14px rgba(0,0,0,.15);overflow:hidden}
.form-panel h2{background:var(--green);color:#fff;font-size:30px;font-weight:900;padding:18px 40px;display:flex;align-items:center;gap:16px}
.form-panel h2 i{width:40px;height:40px;background:#fff;border-radius:6px;display:block}
.form-intro{font-size:16px;line-height:1.8;text-align:center;padding:18px 40px 6px}
.form-table{width:820px;margin:10px auto 0;border-collapse:collapse}
.form-table th,.form-table td{border:1px solid var(--line);padding:8px 14px;font-size:17px;text-align:left}
.form-table th{width:240px;background:#f6f6f6;font-weight:500}
.req{background:#e53935;color:#fff;font-size:13px;padding:2px 8px;border-radius:3px;float:right}
.field{display:inline-block;height:34px;border:1px solid #bbb;border-radius:3px;background:#fff;vertical-align:middle}
.radio{display:inline-flex;align-items:center;gap:6px;margin-right:22px}
.radio i{width:16px;height:16px;border:1px solid #999;border-radius:50%}
.privacy{width:820px;margin:18px auto 0;text-align:center;font-size:16px}
.privacy a{color:var(--blue)}
.btn-submit{display:block;width:420px;margin:22px auto 34px;background:var(--pink);color:#fff;text-align:center;font-size:30px;font-weight:900;border-radius:10px;padding:20px 0;box-shadow:0 5px 0 #b52b5b}

/* access */
.access{top:3960px;height:410px;background:#f3f3f3}
.access-head{text-align:center;padding-top:24px}
.access-head .pin{display:inline-flex;width:60px;height:60px;border-radius:50%;background:var(--green);align-items:center;justify-content:center}
.access-head h2{font-size:32px;font-weight:900;margin-top:6px}
.access-head p{font-size:16px;line-height:1.7;margin-top:6px}
.offices{display:flex;gap:30px;width:860px;margin:18px auto 0}
.office{flex:1;background:#fff;border:1px solid var(--line);display:flex;padding:14px;gap:14px}
.office h3{font-size:18px;color:var(--orange)}
.office p{font-size:14px;line-height:1.6;margin-top:4px}
.office .map{width:200px;height:130px;background:linear-gradient(135deg,#eef1e6,#dfe6d4);flex:none}

/* footer */
.footer{top:4370px;height:62px;background:var(--green);color:#fff;font-size:15px;text-align:center;line-height:62px}
.to-top{position:absolute;right:120px;top:14px;background:#fff;color:var(--green-dark);font-size:14px;line-height:34px;padding:0 16px;border-radius:4px}
.seal{position:absolute;right:40px;top:8px;width:46px;height:46px;border-radius:50%;background:#fff}
</style>
</head>
<body>

<section class="section hero">
  <div class="hero-city" role="img" aria-label="東京の街並みの写真"></div>
  <div class="brand"><span class="dot"></span>モスプリント</div>
  <div class="hero-people" role="img" aria-label="スーツ姿の若い男女の写真"></div>
  <div class="headline">
    <div class="line1"><span class="pref">東京都</span>で正社員求人をお探しの</div>
    <div class="line2">20代のフリーター・既卒</div>
    <div class="line3">未経験から<em>正社員</em>へ</div>
  </div>
  <div class="badge-free">内定だけでなく<br>就職に繋がる<br>カウンセリング<b>¥0</b></div>
  <div class="stats">
    <div class="stat"><h3>サービス利用者</h3><p>34,042<small>人</small></p></div>
    <div class="stat"><h3>未経験OKの求人案件</h3><p>1,000<small>件以上</small></p></div>
    <div class="stat"><h3>内定率</h3><p>78.7<small>%</small></p></div>
  </div>
  <p class="hero-note">あなた専属のコンサルタントが<span class="pref">東京都</span>での就職活動を徹底サポート!</p>
</section>

<section class="section cta">
  <div class="cta-title"><span class="pref-text">東京都</span>で就職カウンセリングを受けるなら<span class="brand"><span class="dot"></span>モスプリント</span></div>
  <div class="cta-row">
    <div class="btn-apply">
      <svg width="44" height="44" viewBox="0 0 44 44"><rect x="4" y="8" width="36" height="28" rx="3" fill="none" stroke="#fff" stroke-width="4"/><path d="M6 10l16 14 16-14" fill="none" stroke="#fff" stroke-width="4"/></svg>
      <span>無料カウンセリング<br>お申し込みはこちら</span>
    </div>
    <div class="tel">
      <div class="tel-icon"><svg width="40" height="40" viewBox="0 0 24 24"><path fill="#fff" d="M6.6 10.8a15.1 15.1 0 006.6 6.6l2.2-2.2c.3-.3.7-.4 1-.2 1.1.4 2.3.6 3.6.6.6 0 1 .4 1 1V20c0 .6-.4 1-1 1A17 17 0 013 4c0-.6.4-1 1-1h3.5c.6 0 1 .4 1 1 0 1.3.2 2.5.6 3.6.1.3 0 .7-.2 1z"/></svg></div>
      <div><small>お電話でのお問い合わせ</small><b>0120-482-617</b><span>受付時間 平日10:00〜19:00</span></div>
    </div>
  </div>
</section>

<section class="section rate">
  <div class="rate-woman" role="img" aria-label="スーツ姿の女性の写真"></div>
  <div class="brand"><span class="dot"></span>モスプリント<span class="nara">なら</span></div>
  <div class="rate-label">就職内定率</div>
  <svg class="rate-chart" width="190" height="190" viewBox="0 0 190 190">
    <circle cx="95" cy="95" r="90" fill="#f5d9a8"/>
    <path d="M95 95 L95 5 A90 90 0 1 1 9.4 67.2 Z" fill="var(--orange)"/>
    <circle cx="95" cy="95" r="45" fill="#fff"/>
  </svg>
  <div class="rate-num">78<small>%以上!</small></div>
  <div class="because"><p>だから</p>
    <svg width="80" height="40" viewBox="0 0 80 40"><path d="M0 0h80L40 40z" fill="var(--green)"/></svg>
  </div>
</section>

<section class="section voices">
  <div class="voices-head">
    <div class="icon"></div>
    <h2>「<span>モスプリント</span>」を利用して就職された方から<br>多くの満足の声をいただいております!</h2>
  </div>
  <div class="voice-list">
    <article class="voice">
      <div class="voice-top">
        <div class="avatar"><svg width="50" height="50" viewBox="0 0 24 24"><circle cx="12" cy="8" r="4" fill="#bbb"/><path d="M4 21c0-5 16-5 16 0z" fill="#bbb"/></svg></div>
        <div><h3>Mさん(23歳)男性</h3><p>前職:アルバイト → 営業職に就職</p></div>
      </div>
      <div class="voice-body">
        <p>高校を卒業してから、アルバイトを続けていましたが、将来が不安になり相談しました。担当の方が親身に話を聞いてくれて、自分に合う仕事を一緒に探してくれました。</p>
        <p>面接の練習や書類の添削も丁寧にしていただき、初めての就職活動でも安心して進めることができました。</p>
        <p>今は営業職として毎日充実しています。もっと早く相談すればよかったと思っています。</p>
      </div>
    </article>
    <article class="voice">
      <div class="voice-top">
        <div class="avatar"><svg width="50" height="50" viewBox="0 0 24 24"><circle cx="12" cy="8" r="4" fill="#bbb"/><path d="M4 21c0-5 16-5 16 0z" fill="#bbb"/></svg></div>
        <div><h3>Kさん(25歳)女性</h3><p>前職:フリーター → 事務職に就職</p></div>
      </div>
      <div class="voice-body">
        <p>大学を中退してから正社員の経験がなく、応募できる会社があるのか心配でした。カウンセリングで自分の強みを見つけてもらえました。</p>
        <p>未経験でも応募できる求人を多く紹介していただき、面接後のフォローもとても心強かったです。</p>
        <p>事務職として働き始め、毎日新しいことを学んでいます。本当に感謝しています。</p>
      </div>
    </article>
  </div>
</section>

<section class="section form">
  <div class="form-bg" role="img" aria-label="オフィス街の写真"></div>
  <div class="form-panel">
    <h2><i></i>無料カウンセリングのお申し込みはこちら</h2>
    <p class="form-intro">下記のフォームに必要事項をご入力の上、お申し込みください。<br>担当者より2営業日以内にご連絡いたします。お気軽にどうぞ。</p>
    <table class="form-table">
      <tr><th>お名前<span class="req">必須</span></th><td><span class="field" style="width:180px"></span> <span class="field" style="width:180px"></span></td></tr>
      <tr><th>ふりがな<span class="req">必須</span></th><td><span class="field" style="width:180px"></span> <span class="field" style="width:180px"></span></td></tr>
      <tr><th>性別<span class="req">必須</span></th><td><span class="radio"><i></i>男性</span><span class="radio"><i></i>女性</span></td></tr>
      <tr><th>最終学歴<span class="req">必須</span></th><td><span class="field" style="width:260px"></span></td></tr>
      <tr><th>生年月日<span class="req">必須</span></th><td><span class="field" style="width:100px"></span> 年 <span class="field" style="width:70px"></span> 月 <span class="field" style="width:70px"></span> 日</td></tr>
      <tr><th>お住まい<span class="req">必須</span></th><td><span class="field" style="width:200px"></span></td></tr>
      <tr><th>お電話番号(携帯可)<span class="req">必須</span></th><td><span class="field" style="width:320px"></span></td></tr>
      <tr><th>メールアドレス<span class="req">必須</span></th><td><span class="field" style="width:420px"></span></td></tr>
      <tr><th>ご質問等</th><td><span class="field" style="width:520px;height:100px"></span></td></tr>
    </table>
    <p class="privacy">こちらをご確認ください ⇒ <a>個人情報の取り扱い</a></p>
    <div class="btn-submit">上記に同意して応募する ›</div>
  </div>
</section>

<section class="section access">
  <div class="access-head">
    <span class="pin"><svg width="30" height="30" viewBox="0 0 24 24"><path fill="#fff" d="M12 2a7 7 0 00-7 7c0 5 7 13 7 13s7-8 7-13a7 7 0 00-7-7zm0 9.5A2.5 2.5 0 1112 6a2.5 2.5 0 010 5z"/></svg></span>
    <h2>アクセス</h2>
    <p>モスプリントの就職カウンセリングは以下2拠点にて受け付けております。<br>どちらも駅から5分以内にアクセス可能です。</p>
  </div>
  <div class="offices">
    <div class="office">
      <div><h3>本社(千代田区)</h3><p>東京都千代田区神田小川町<br>3-9-1 5階<br>神保町駅より徒歩4分</p></div>
      <div class="map" role="img" aria-label="本社周辺の地図"></div>
    </div>
    <div class="office">
      <div><h3>池袋支店</h3><p>東京都豊島区南池袋<br>2-40-8 3階<br>池袋駅より徒歩5分</p></div>
      <div class="map" role="img" aria-label="池袋支店周辺の地図"></div>
    </div>
  </div>
</section>

<footer class="section footer">
  © 2014 Mosuplint Co., Ltd.
  <span class="to-top">ページ上部へ戻る</span>
  <span class="seal"></span>
</footer>

</body>
</html>
```